Brackenmoor.com.au - Quorvel Australia - Uncoded PSD only

We need a web design for a virtual assistant company based in Sydney Australia called "Brackenmoor". We provide virtual assistance and unlimited admin tasks to small business owners for a monthly fee. We would like to see designs that are not too different to www.quorvel.com. Words to describe the design and feel of this website are sleek and professional. We want to use bright inviting colours for the call to action buttons and a professional business focused background.

Target Market(s)

business executives, business owners, small business owners, those professionals who lack time.

Industry/Entity Type

Business Consultant

Number of Pages Required

3 page

Font styles to use
Sans Serif

Colors
5e5e5e
1b1b1b
3176b5
33b8a4

Requirements
Must have
• Call to action buttons, sleek business feel think plovix.io and quorvel.com
Nice to have
• Bold back ground colours, bright call to action buttons
Should not have
• too much white

```html
<!DOCTYPE html>
<html lang="en">
<head>
<meta charset="utf-8">
<title>Brackenmoor – Virtual Assistance</title>
<link href="https://fonts.googleapis.com/css2?family=Lato:wght@300;400;700;900&display=swap" rel="stylesheet">
<style>
:root{
  --blue:#3176b5;
  --teal:#33b8a4;
  --ink:#1b1b1b;
  --grey:#5e5e5e;
  --light:#f4f6f8;
  --white:#ffffff;
  --footer:#1e1f22;
  --footer-deep:#151618;
}
*{box-sizing:border-box;margin:0;padding:0}
html,body{width:1200px;height:2476px;overflow:hidden}
body{font-family:"Lato",Arial,sans-serif;color:var(--grey);background:var(--white);position:relative}
.btn{display:inline-block;background:var(--blue);color:var(--white);font-size:15px;font-weight:700;padding:11px 24px;border-radius:3px;text-decoration:none}

/* header */
.site-header{position:absolute;top:0;left:0;width:1200px;height:92px;background:rgba(255,255,255,.96);display:flex;align-items:center;justify-content:space-between;padding:0 60px;z-index:2}
.brand{font-size:30px;font-weight:900;color:var(--blue);letter-spacing:1px;display:flex;align-items:center;gap:12px}
.brand-mark{width:14px;height:14px;background:var(--blue)}
.main-nav{display:flex;align-items:center;gap:30px;font-size:15px;color:var(--grey)}
.main-nav .active{color:var(--blue);font-weight:700;border-bottom:2px solid var(--blue);padding-bottom:4px}
.main-nav .login{background:var(--blue);color:var(--white);padding:10px 26px;border-radius:3px;font-weight:700}

/* hero */
.hero{position:absolute;top:0;left:0;width:1200px;height:540px}
.hero-photo{position:absolute;inset:0;background:linear-gradient(100deg,#5b6672 0%,#9aa6b1 35%,#d9dee3 60%,#b4bcc4 100%)}
.hero-box{position:absolute;left:0;top:300px;width:470px;height:190px;background:rgba(20,30,40,.62);padding:28px 40px}
.hero-box h1{font-size:34px;font-weight:700;color:var(--white);margin-bottom:10px}
.hero-box p{font-size:14px;color:#e4e8ec;line-height:1.5;margin-bottom:18px}

/* call band */
.call-band{position:absolute;top:540px;left:0;width:1200px;height:100px;background:var(--teal);display:flex;align-items:center;justify-content:space-between;padding:0 60px}
.call-band h2{font-size:28px;font-weight:700;color:var(--white)}
.call-band p{font-size:15px;color:#eafaf7;margin-top:4px}
.call-band .btn{padding:12px 34px}

/* features */
.features{position:absolute;top:640px;left:0;width:1200px;height:330px;background:var(--white);display:flex;justify-content:center;gap:40px;padding-top:70px}
.feature{width:230px;text-align:center}
.feature-icon{width:72px;height:72px;margin:0 auto 18px;border-radius:8px}
.feature h3{font-size:17px;font-weight:700;color:var(--ink);margin-bottom:8px}
.feature h3.accent{color:var(--teal)}
.feature p{font-size:12px;line-height:1.5}

/* welcome */
.welcome{position:absolute;top:975px;left:0;width:1200px;height:425px;display:flex}
.welcome-text{width:600px;background:var(--teal);padding:70px 60px 0 110px;color:var(--white)}
.welcome-text h2{font-size:38px;font-weight:400;margin-bottom:22px}
.welcome-text p{font-size:15px;line-height:1.5;margin-bottom:22px;color:#f0fbf9}
.welcome-photo{width:600px;background:linear-gradient(135deg,#1c3f66 0%,#3d7fb8 45%,#c9d4dc 100%)}

/* who we are */
.who{position:absolute;top:1400px;left:0;width:1200px;height:425px;display:flex;background:var(--light)}
.who-photo{width:480px;background:linear-gradient(120deg,#2b3036 0%,#6a7079 50%,#c5c9cd 100%)}
.who-text{flex:1;padding:40px 80px 0 50px}
.who-text h2{font-size:30px;font-weight:900;color:var(--ink);margin-bottom:18px}
.who-text p{font-size:13px;line-height:1.6;margin-bottom:16px}

/* testimonial */
.testimonial{position:absolute;top:1832px;left:0;width:1200px;height:328px;background:linear-gradient(90deg,#7b8894 0%,#b9c3cb 50%,#8a97a2 100%);text-align:center;padding-top:40px}
.avatar{width:80px;height:80px;border-radius:50%;background:#e6e9ec;border:3px solid var(--white);margin:0 auto 18px}
.testimonial blockquote{font-size:15px;color:var(--ink);line-height:1.5;width:560px;margin:0 auto 26px}
.testimonial cite{font-style:normal;font-size:18px;font-weight:700;color:var(--ink)}
.arrow{position:absolute;top:140px;width:44px;height:34px;background:var(--blue)}
.arrow.prev{left:100px}.arrow.next{left:1030px;background:transparent}
.arrow svg{display:block;margin:7px auto}

/* footer */
.site-footer{position:absolute;top:2160px;left:0;width:1200px;height:316px;background:var(--footer);color:#b9bcc0}
.footer-cols{display:flex;padding:50px 110px 0;gap:60px;height:260px}
.footer-col{width:220px;font-size:12px;line-height:1.6}
.footer-col h4{font-size:18px;font-weight:700;color:var(--white);margin-bottom:18px}
.footer-col ul{list-style:none}
.footer-col li{margin-bottom:6px}
.footer-col li.current{color:var(--teal)}
.contact-row{display:flex;align-items:center;gap:10px;margin-bottom:12px}
.contact-row svg{flex:none}
.field{height:28px;background:var(--white);border-radius:2px;margin-bottom:8px;font-size:11px;color:#999;padding:6px 10px}
.submit{display:inline-block;background:var(--blue);color:var(--white);font-size:12px;padding:6px 18px;border-radius:2px}
.footer-bar{height:56px;background:var(--footer-deep);display:flex;align-items:center;justify-content:space-between;padding:0 110px;font-size:12px}
.socials{display:flex;gap:8px}
.socials span{width:20px;height:20px;border-radius:50%;background:var(--blue)}
.socials span:nth-child(2){background:var(--teal)}
.socials span:nth-child(3){background:#c2473a}
</style>
</head>
<body>

<header class="site-header">
  <div class="brand"><span class="brand-mark"></span>BRACKENMOOR</div>
  <nav class="main-nav">
    <span class="active">Home</span><span>About Us</span><span>Service</span><span>Testimonial</span><span>Contact Us</span><span class="login">Login</span>
  </nav>
</header>

<section class="hero">
  <div class="hero-photo" role="img" aria-label="Business professionals in a bright office reviewing documents together"></div>
  <div class="hero-box">
    <h1>Welcome To BRACKENMOOR</h1>
    <p>Lorem ipsum dolor sit amet, consectetur adipiscing elit. Pellentesque tristique dui at fermentum urna, vitae porta lectus.</p>
    <span class="btn">Request A Consultation</span>
  </div>
</section>

<section class="call-band">
  <div>
    <h2>Are you having any problems but can't consult to anyone?</h2>
    <p>Talk to us! We promise we can help you! Call Now! (02) 5550 1040</p>
  </div>
  <span class="btn">Contact Now</span>
</section>

<section class="features">
  <div class="feature">
    <div class="feature-icon" style="background:#d9403a" role="img" aria-label="Gift box icon"></div>
    <h3>Run Competitions</h3>
    <p>Lorem ipsum dolor sit amet, consectetur adipiscing elit. Pellentesque tristique dui at facilisis porta.</p>
  </div>
  <div class="feature">
    <div class="feature-icon" style="background:#f0b23a" role="img" aria-label="Envelope icon"></div>
    <h3>Capture Emails</h3>
    <p>Lorem ipsum dolor sit amet, consectetur adipiscing elit. Pellentesque tristique dui at facilisis porta.</p>
  </div>
  <div class="feature">
    <div class="feature-icon" style="background:#7b4fc9" role="img" aria-label="Camera icon"></div>
    <h3 class="accent">Visual Galleries</h3>
    <p>Lorem ipsum dolor sit amet, consectetur adipiscing elit. Pellentesque tristique dui at facilisis porta.</p>
  </div>
  <div class="feature">
    <div class="feature-icon" style="background:#8c2430" role="img" aria-label="Trophy icon"></div>
    <h3>Redeem Rewards</h3>
    <p>Lorem ipsum dolor sit amet, consectetur adipiscing elit. Pellentesque tristique dui at facilisis porta.</p>
  </div>
</section>

<section class="welcome">
  <div class="welcome-text">
    <h2>Welcome To Brackenmoor</h2>
    <p>Lorem ipsum dolor sit amet, consectetur adipiscing elit. Nunc suscipit pulvinar dolor, ac fermentum neque faucibus sed. Duis in vehicula diam.<br>Curabitur dictum porttitor risus, a egestas libero. Nullam vitae hendrerit dolor sed posuere.</p>
    <span class="btn">Read More</span>
  </div>
  <div class="welcome-photo" role="img" aria-label="Person working on a laptop with digital marketing graphics and a cup of coffee"></div>
</section>

<section class="who">
  <div class="who-photo" role="img" aria-label="Businessman in a dark suit adjusting his jacket"></div>
  <div class="who-text">
    <h2>WHO WE ARE</h2>
    <p>Lorem ipsum dolor sit amet, consectetur adipiscing elit. Pellentesque tristique dui at facilisis porta. Vivamus a nunc ut ligula consequat dictum. Mauris sagittis libero at lacus malesuada, sed viverra lectus gravida. Nulla facilisi. Donec at felis non neque porta rutrum.</p>
    <p>Quisque vitae ligula non arcu, at tempus sapien vehicula. Aenean ornare purus mollis, id elementum tortor volutpat. Etiam nec augue quis lorem vehicula sodales. Aliquam erat volutpat. Sed vitae rhoncus enim, at porta massa. Curabitur non tellus sed nulla aliquet posuere sit amet eget mi.</p>
    <span class="btn">Read More</span>
  </div>
</section>

<section class="testimonial">
  <div class="testimonial-bg"></div>
  <div class="avatar" role="img" aria-label="Client portrait"></div>
  <blockquote>Lorem ipsum dolor sit amet, consectetur adipiscing elit. Proin ac ultricies dui, finibus sagittis consectetur dolor.</blockquote>
  <cite>Maren Holloway</cite>
  <span class="arrow prev"><svg width="14" height="20" viewBox="0 0 14 20"><path d="M11 2 3 10l8 8" fill="none" stroke="#fff" stroke-width="3"/></svg></span>
  <span class="arrow next"><svg width="14" height="20" viewBox="0 0 14 20"><path d="m3 2 8 8-8 8" fill="none" stroke="#3176b5" stroke-width="3"/></svg></span>
</section>

<footer class="site-footer">
  <div class="footer-cols">
    <div class="footer-col">
      <h4>About us</h4>
      <p>We provide our customers with the best service at the best prices. We aim to be Southern Africa's leading online spa retailer with a network of independent agencies in the whole of Southern Africa. <span style="color:var(--teal)">Read More</span></p>
    </div>
    <div class="footer-col">
      <h4>Main menu</h4>
      <ul><li>Home</li><li>About Us</li><li>Service</li><li class="current">Testimonial</li><li>Contact Us</li></ul>
    </div>
    <div class="footer-col">
      <h4>Contact us</h4>
      <div class="contact-row"><svg width="20" height="20" viewBox="0 0 20 20"><circle cx="10" cy="10" r="9" fill="none" stroke="#b9bcc0"/><path d="M10 5a3 3 0 0 0-3 3c0 2.5 3 6 3 6s3-3.5 3-6a3 3 0 0 0-3-3z" fill="#b9bcc0"/></svg><span>12 Harbour Lane, Sydney<br>NSW 2000 Australia</span></div>
      <div class="contact-row"><svg width="20" height="20" viewBox="0 0 20 20"><circle cx="10" cy="10" r="9" fill="none" stroke="#b9bcc0"/><path d="M7 6h2l1 2-1 1a5 5 0 0 0 2 2l1-1 2 1v2c-4 0-7-3-7-7z" fill="#b9bcc0"/></svg><span>(02) 5550 1040</span></div>
      <div class="contact-row"><svg width="20" height="20" viewBox="0 0 20 20"><circle cx="10" cy="10" r="9" fill="none" stroke="#b9bcc0"/><rect x="5.5" y="7" width="9" height="6" fill="none" stroke="#b9bcc0"/><path d="m5.5 7 4.5 3.5L14.5 7" fill="none" stroke="#b9bcc0"/></svg><span>info@brackenmoor.com.au</span></div>
    </div>
    <div class="footer-col">
      <h4>Newsletter</h4>
      <div class="field">Your Name</div>
      <div class="field">Email</div>
      <span class="submit">Submit</span>
    </div>
  </div>
  <div class="footer-bar">
    <span>Copyright © 2015. brackenmoor.com.au</span>
    <div class="socials"><span></span><span></span><span></span><span></span></div>
  </div>
</footer>

</body>
</html>
```